Brightwater Charity Ball Poster

We are looking for a poster for our upcoming event, "Brightwater Charity Ball" - a sit down dinner formal event hosted by our university club, OKRU.
Usually we source designs internally from our committee (even if they aren't the most amazing quality), however this time round we have no one available to do it as everyone is a volunteer.
The event's theme is 'winter wonderland', based around the snowy forests you see in Veltmoor or Crown of Ashes (neither of these specific things are the theme however). Our venue is a clear-roof marque in a space surrounded by very tall pine trees giving off the forest vibe, and there are festoons strung between the trees so this is an element of warm light amongst the forest, perhaps a building or village tucked away in the forest.
The poster is for printing out at A3 size, and we will also need to create a Facebook event cover photo and other marketing graphics from the original poster files so some flexibility in the design and original files are required.
Things that need to be included on the poster :
---Event details
Brightwater Charity Ball
Saturday 12th August
7pm – midnight
Halberd Auditorium, KPC
Tables of 10
Members - $140
Non members - $150
All profits donated to Stride for Hope
---- Extra info and images (can be at the bottom, in corners etc,)
18+ ID required | Drink Responsibly
OKRU Logo
KPC Union Logo
(these logos may be changed to black and white if need be)
Example images of styles, colours and the sort of landscape we want for the poster can be found in the document attached.

```html
<!DOCTYPE html>
<html lang="en">
<head>
<meta charset="utf-8">
<title>Brightwater Charity Ball</title>
<link rel="stylesheet" href="https://fonts.googleapis.com/css2?family=Questrial&family=Raleway:wght@600;700&family=Yellowtail&display=swap">
<style>
  :root {
    --maroon: #7a2343;
    --ink: #2a2628;
    --white: #ffffff;
    --rule: #b58a98;
    --forest-dark: #2a1a1c;
    --forest-warm: #8a4a48;
    --snow: #f6f1f3;
    --muted: rgba(42,38,40,0.4);
  }
  * { margin: 0; padding: 0; box-sizing: border-box; }
  html, body { width: 849px; height: 1200px; overflow: hidden; background: var(--white); }
  .poster {
    position: relative;
    width: 849px;
    height: 1200px;
    font-family: "Questrial", sans-serif;
    color: var(--ink);
    overflow: hidden;
  }
  .scene {
    position: absolute;
    left: 0; top: 0;
    width: 849px; height: 1058px;
    background:
      radial-gradient(ellipse 340px 300px at 420px 330px, rgba(156,58,92,0.75), rgba(156,58,92,0) 100%),
      radial-gradient(ellipse 520px 360px at 424px 1000px, var(--snow) 30%, rgba(246,241,243,0) 100%),
      linear-gradient(90deg, var(--forest-dark) 0%, rgba(42,26,28,0.2) 30%, rgba(42,26,28,0) 50%, rgba(42,26,28,0.2) 70%, var(--forest-dark) 100%),
      linear-gradient(180deg, #3a2224 0%, var(--forest-warm) 35%, #c9aeb4 60%, var(--snow) 85%);
  }
  .client {
    position: absolute;
    top: 104px; left: 0; width: 849px;
    display: flex; justify-content: center; align-items: center; gap: 12px;
    color: var(--white);
  }
  .client-dot { width: 14px; height: 14px; border-radius: 50%; background: var(--white); }
  .client-name { font-size: 58px; letter-spacing: 4px; line-height: 1; }
  .centered { position: absolute; left: 0; width: 849px; text-align: center; }
  .presents { top: 246px; font-size: 24px; color: var(--white); letter-spacing: 1px; }
  .title {
    top: 262px;
    font-family: "Yellowtail", cursive;
    font-weight: 400;
    font-size: 124px;
    line-height: 1;
    color: var(--white);
    text-shadow: 0 3px 6px rgba(40,10,20,0.35);
  }
  .subtitle { top: 386px; font-size: 39px; color: var(--white); letter-spacing: 1px; }
  .details { top: 664px; font-size: 23px; line-height: 29px; }
  .pricing { top: 780px; font-size: 23px; line-height: 29px; }
  .pricing .label { font-family: "Raleway", sans-serif; font-weight: 600; color: var(--maroon); }
  .cause {
    top: 896px;
    font-family: "Raleway", sans-serif; font-weight: 700;
    font-size: 27px; line-height: 35px; color: var(--maroon);
  }
  .notice { top: 995px; font-size: 17px; }
  .footer {
    position: absolute; left: 0; top: 1058px;
    width: 849px; height: 142px; background: var(--white);
  }
  .footer-heading { position: absolute; top: 23px; font-size: 18px; color: var(--maroon); letter-spacing: 0.5px; }
  .heading-partner { left: 46px; }
  .heading-sponsors { left: 450px; }
  .rule { position: absolute; top: 34px; height: 1px; background: var(--rule); }
  .rule-left { left: 242px; width: 196px; }
  .rule-right { left: 616px; width: 196px; }
  .sponsor {
    display: flex; align-items: center; gap: 6px;
    font-size: 12px; color: var(--ink); line-height: 1.25;
  }
  .sponsor-mark { width: 12px; height: 12px; flex: none; background: var(--maroon); }
  .sponsor-mark.round { border-radius: 50%; }
  .partner { position: absolute; left: 56px; top: 72px; width: 150px; }
  .sponsor-row {
    position: absolute; left: 232px; top: 66px; width: 580px;
    display: flex; justify-content: space-between; align-items: center;
  }
  .sponsor-row .sponsor { width: 108px; }
  .placeholder-note {
    position: absolute; left: 232px; top: 112px; width: 580px;
    text-align: center; font-size: 13px; color: var(--muted); letter-spacing: 2px;
  }
</style>
</head>
<body>
<main class="poster">
  <div class="scene" role="img" aria-label="Snowy forest path at dusk lined with tall frosted trees and a warm glow between them"></div>

  <div class="client">
    <span class="client-dot"></span>
    <span class="client-name">OKRU</span>
  </div>

  <p class="centered presents">PRESENTS THE</p>
  <h1 class="centered title">Brightwater</h1>
  <p class="centered subtitle">CHARITY BALL</p>

  <p class="centered details">Saturday, August 12th<br>7pm - Midnight<br>Halberd Auditorium, KPC</p>

  <p class="centered pricing"><span class="label">Tables of 10</span><br>Members - $140<br>Non Members - $150</p>

  <p class="centered cause">ALL PROCEEDS TO<br>STRIDE FOR HOPE KPC</p>

  <p class="centered notice">18+ ID Required | Drink Responsibly</p>

  <footer class="footer">
    <span class="footer-heading heading-partner">MAJOR PARTNER</span>
    <span class="rule rule-left"></span>
    <span class="footer-heading heading-sponsors">EVENT SPONSORS</span>
    <span class="rule rule-right"></span>

    <div class="sponsor partner"><span class="sponsor-mark"></span><span>Larkfield Event Hire</span></div>

    <div class="sponsor-row">
      <div class="sponsor"><span class="sponsor-mark round"></span><span>Marlow Photo &amp; Film</span></div>
      <div class="sponsor"><span>Dorian Vale Photographer</span></div>
      <div class="sponsor"><span class="sponsor-mark round"></span><span>Keystone Security<br>keystone.example</span></div>
      <div class="sponsor"><span>The Copper Kettle</span></div>
      <div class="sponsor"><span class="sponsor-mark"></span><span>KPC Union</span></div>
    </div>
    <span class="placeholder-note">[PLACEHOLDERS ONLY]</span>
  </footer>
</main>
</body>
</html>
```